Letterhead to Prospective Clients

Create a letterhead (word & canva) that I will use to send letters to prospective clients and also include the Coralwood Estate Partners Logo, My Contact Details and Interchangeable "Suburb". Use the same font and colour pallete

Maris Dulworth | "Suburb" Specialist - Redlands & Surrounds
Mobile: 0417 862 095
Email: MD@CoralwoodEstatePartners.com.au

```html
<!DOCTYPE html>
<html lang="en">
<head>
<meta charset="utf-8">
<title>Coralwood Estate Partners — Letterhead</title>
<link href="https://fonts.googleapis.com/css2?family=Arimo:wght@400;700&display=swap" rel="stylesheet">
<style>
  :root {
    --navy: #0c1a3f;
    --tan: #a3826b;
    --mist: #ececec;
    --paper: #ffffff;
    --backdrop: #d9d9dc;
  }
  * { margin: 0; padding: 0; box-sizing: border-box; }
  html, body {
    width: 1200px;
    height: 1179px;
    overflow: hidden;
    background: var(--backdrop);
    font-family: "Arimo", Arial, sans-serif;
    color: var(--navy);
  }
  .letterhead {
    position: absolute;
    left: 239px;
    top: 89px;
    width: 712px;
    height: 1007px;
    background: var(--paper);
    overflow: hidden;
  }
  .brand {
    position: absolute;
    left: 50px;
    top: 44px;
    width: 260px;
    text-align: center;
    color: var(--navy);
    font-weight: 400;
  }
  .brand-name {
    display: block;
    font-size: 35px;
    line-height: 42px;
    letter-spacing: 2px;
  }
  .brand-tagline {
    display: block;
    margin-top: 16px;
    font-size: 8.5px;
    letter-spacing: 3px;
  }
  .contact {
    position: absolute;
    left: 446px;
    top: 45px;
    width: 204px;
    font-size: 10.5px;
    line-height: 13px;
  }
  .contact-name {
    font-size: 12.5px;
    line-height: 15px;
    font-weight: 700;
  }
  .contact-role { font-size: 10.5px; }
  .contact-rule {
    margin: 7px 0 6px;
    border: 0;
    border-top: 1px solid var(--navy);
  }
  .contact-line {
    display: flex;
    align-items: center;
    gap: 5px;
  }
  .contact-line svg { flex: none; }
  .footer-band {
    position: absolute;
    left: 0;
    bottom: 0;
    width: 100%;
    height: 52px;
    background: linear-gradient(100deg, var(--tan) 0%, var(--tan) 35%, var(--navy) 70%, var(--navy) 100%);
  }
</style>
</head>
<body>
  <main class="letterhead">
    <div class="brand">
      <span class="brand-name">CORALWOOD</span>
      <span class="brand-tagline">ESTATE PARTNERS</span>
    </div>

    <div class="contact">
      <p class="contact-name">MARIS DULWORTH</p>
      <p class="contact-role">"Suburb" Specialist - Redlands &amp; Surrounds</p>
      <hr class="contact-rule">
      <p class="contact-line">
        <svg width="10" height="10" viewBox="0 0 10 10" aria-hidden="true">
          <rect x="2.5" y="0.8" width="5" height="8.4" rx="1" fill="none" stroke="var(--tan)" stroke-width="1.1"/>
        </svg>
        <span>0417 862 095</span>
      </p>
      <p class="contact-line">
        <svg width="10" height="10" viewBox="0 0 10 10" aria-hidden="true">
          <rect x="0.5" y="2" width="9" height="6" fill="var(--tan)"/>
          <path d="M0.8 2.3 L5 5.6 L9.2 2.3" fill="none" stroke="#fff" stroke-width="0.9"/>
        </svg>
        <span>MD@CoralwoodEstatePartners.com.au</span>
      </p>
    </div>

    <div class="footer-band" role="img" aria-label="Decorative footer band in brand tan and navy"></div>
  </main>
</body>
</html>
```